Letter Head for accounting firm

We need letter head designed using our attached logo.

We also need the following information on the letterhead:

482 E Mill Rd. Danvers, OH 43762

HarborLedgerLtd.com

1-855-613-2907

Contact Information for Business Card

Use logo

Colors

Designer to choose colors to be used in the design.

Requirements
Must have
• Business Card - Should also have name and title - email address

```html
<!DOCTYPE html>
<html lang="en">
<head>
<meta charset="utf-8">
<title>Harbor Ledger Group Ltd — Letterhead</title>
<link rel="stylesheet" href="https://fonts.googleapis.com/css2?family=Lato:wght@400;700&family=Yellowtail&display=swap">
<style>
  :root {
    --brand-blue: #1480c8;
    --brand-navy: #23262f;
    --ink: #3a3a3a;
    --ink-soft: #555555;
    --paper: #ffffff;
    --backdrop: #e6e6e8;
    --divider: #b9b9b9;
  }
  * { box-sizing: border-box; margin: 0; padding: 0; }
  html, body {
    width: 996px; height: 1200px; overflow: hidden;
    background: var(--backdrop);
    font-family: "Lato", Arial, sans-serif;
  }
  .letterhead {
    position: absolute; left: 73px; top: 0;
    width: 850px; height: 1200px;
    background: var(--paper);
    overflow: hidden;
  }
  .brand {
    position: absolute; left: 62px; top: 82px;
    display: flex; align-items: center; gap: 12px;
  }
  .brand-square {
    width: 34px; height: 34px; background: var(--brand-blue);
  }
  .brand-name {
    color: var(--brand-blue); font-weight: 700; font-size: 18px;
    line-height: 1.2; letter-spacing: 0.2px;
  }
  .contact {
    position: absolute; left: 567px; top: 68px;
    border-left: 1.5px solid var(--divider);
    padding: 2px 0 2px 10px;
    font-size: 16px; color: var(--brand-navy);
  }
  .contact-row { display: flex; align-items: center; gap: 8px; height: 26px; }
  .contact-row svg { width: 14px; height: 14px; flex: none; }
  .letter {
    position: absolute; left: 63px; top: 312px; width: 731px;
  }
  .salutation {
    color: var(--brand-blue); font-weight: 700; font-size: 16px; margin-bottom: 22px;
  }
  .letter p {
    font-size: 16px; line-height: 25.6px; color: var(--ink-soft);
    text-align: justify; margin-bottom: 19px;
  }
  .closing { font-size: 19px; color: var(--brand-navy); margin-top: 33px; }
  .signature {
    font-family: "Yellowtail", cursive;
    color: var(--brand-blue); font-size: 38px; margin-top: 4px;
  }
  .footer-wave { position: absolute; left: 0; top: 1058px; width: 850px; height: 142px; }
  .address {
    position: absolute; right: 33px; bottom: 22px;
    display: flex; align-items: center; gap: 8px;
    color: #ffffff; font-size: 17px;
  }
  .address svg { width: 12px; height: 16px; }
</style>
</head>
<body>
  <main class="letterhead">
    <header>
      <div class="brand">
        <span class="brand-square"></span>
        <span class="brand-name">HARBOR LEDGER GROUP<br>LTD</span>
      </div>
      <div class="contact">
        <div class="contact-row">
          <svg viewBox="0 0 14 14"><circle cx="7" cy="7" r="6.2" fill="none" stroke="#1480c8" stroke-width="1.2"/><path d="M5 3.5c-.8.4-1.1 1.4-.6 2.6.6 1.6 1.8 3 3.2 3.8.9.5 1.8.4 2.2-.3l-1.3-1.2-.8.5c-.8-.4-1.5-1.2-1.9-2l.5-.8z" fill="#1480c8"/></svg>
          <span>1-855-613-2907</span>
        </div>
        <div class="contact-row">
          <svg viewBox="0 0 14 14" fill="none" stroke="#1480c8" stroke-width="1"><circle cx="7" cy="7" r="6"/><ellipse cx="7" cy="7" rx="2.6" ry="6"/><path d="M1 7h12M2 4h10M2 10h10"/></svg>
          <span>www.harborledgerltd.com</span>
        </div>
      </div>
    </header>

    <section class="letter">
      <div class="salutation">Dear Mr. Lorem,</div>
      <p>Lorem ipsum dolor sit amet, consectetuer adipiscing elit, sed diam nonummy nibh euismod tincidunt ut laoreet dolore magna aliquam erat volutpat. Ut wisi enim ad minim veniam, quis nostrud exerci tation ullamcorper suscipit lobortis nisl ut aliquip ex ea commodo consequat. Duis autem vel eum iriure dolor in hendiusto odio dignissim qui blandit praesent luptatum zzril delenit augue duis dolore te feugait nulla facilisi.</p>
      <p>Lorem ipsum dolor sit amet, consectetuer adipiscing elit, sed diam nonummy nibh euismod tincidunt ut laoreet dolore magna aliquam erat volutpat. Ut wisi enim ad minim veniam, quis nostrud exerci tation ullamcorper suscipit lobortis nisl ut aliquip ex ea commodo consequat. Duis autem vel eum iriure dolor in hendiusto odio dignissim qui blandit praesent luptatum zzril delenit augue duis dolore te feugait nulla facilisi.</p>
      <p>Lorem ipsum dolor sit amet, consectetuer adipiscing elit, sed diam nonummy nibh euismod tincidunt ut laoreet dolore magna aliquam erat volutpat. Ut wisi enim ad minim veniam, quis nostrud exerci tation ullamcorper suscipit lobortis nisl ut aliquip ex ea commodo consequat. Duis autem vel eum iriure dolor in hendiusto odio dignissim qui blandit praesent luptatum zzril delenit augue duis dolore te feugait nulla facilisi.</p>
      <div class="closing">Sincerely Your,</div>
      <div class="signature">Your Name</div>
    </section>

    <footer>
      <svg class="footer-wave" viewBox="0 0 850 142" preserveAspectRatio="none">
        <path d="M0 28 C70 75 170 112 330 118 C520 124 660 62 850 52 L850 142 L0 142 Z" fill="var(--brand-blue)"/>
        <path d="M0 42 C80 92 190 116 340 120 C480 122 600 88 720 70" fill="none" stroke="#ffffff" stroke-width="5"/>
        <path d="M70 96 C160 128 300 134 420 122 C540 110 640 76 700 66 C620 86 530 116 420 128 C300 140 170 130 70 96 Z" fill="var(--brand-navy)"/>
        <path d="M620 70 C700 52 790 44 850 48" fill="none" stroke="#ffffff" stroke-width="3"/>
        <path d="M0 0 L0 28 C10 34 20 40 28 44 C18 34 8 20 0 0 Z" fill="var(--brand-blue)"/>
      </svg>
      <div class="address">
        <svg viewBox="0 0 12 16"><path d="M6 0C2.7 0 0 2.6 0 5.9 0 10.3 6 16 6 16s6-5.7 6-10.1C12 2.6 9.3 0 6 0zm0 8.2A2.3 2.3 0 1 1 6 3.6a2.3 2.3 0 0 1 0 4.6z" fill="#ffffff"/></svg>
        <span>482 E Mill Rd. Danvers, OH 43762</span>
      </div>
    </footer>
  </main>
</body>
</html>
```